Harvest Lantern Ministry Conference

I am in need of promotional graphics for our upcoming event. This event, titled "Harbor Crest Youth Conference", is a weekend event for teenagers 11-19 years old. They hear from religious speakers, listen to a band, and do other fun activities. Graphic design should be geared to young adults/older teens. Alcohol, drugs, smoking are not permitted. Open to any color combinations you think fit with your design.
Event Info:
November 1-3, 2024
Tellwood Exhibit Hall, Sioux Falls, SD
Speakers: Marcus Linden (man in light blue shirt in attached photo), Tessa Vandermeer (woman in attached photo), Colin Hardy ( man in dark colored shirt in attached photo)
Worship: KW Collective
HarborCrestGather.com
#742GR
Our Organization Logo (attached): Lumenward
Once designed, I need the following graphics file sizes:
-11x17 Vertical Poster design: include all event info AND a "blank" space on the bottom or box for groups to add their own details/information. Also include the QRV logo and our organization logo Lumenward in some way.
-Make an additional copy of the 11x17 pdf with cut and bleed lines for printing, please.
-4x3 horizontal postcard: include all event info on 1 side including Lumenward logo and QRV; blank backside
-Main Graphic Slide: formatted to fit a widescreen 16x9 screen. Include event name, hashtag, QRV and Lumenward logo
-social media graphic(s) for event: can incorporate some or all of the event details. WILLING TO ADJUST BUDGET FOR SOCIAL MEDIA graphics.
-4.25in x 2.75in vertical badge: include event title on front with Lumenward logo
Target Market
ages 11-19
Target Market(s)
11-19 years old
Industry/Entity Type
Christian Youth Ministry

```html
<!DOCTYPE html>
<html lang="en">
<head>
<meta charset="UTF-8">
<title>Harbor Crest Youth Conference – Poster</title>
<link rel="stylesheet" href="https://fonts.googleapis.com/css2?family=Poppins:wght@400;500;700;800&display=swap">
<style>
  :root{
    --navy:#0d0f3a;
    --royal:#2b3486;
    --indigo:#3b4597;
    --sky:#7aaed8;
    --paper:#f1f2f4;
    --ink:#1b1b1f;
    --white:#ffffff;
    --pin:#e3202b;
  }
  *{margin:0;padding:0;box-sizing:border-box}
  html,body{width:706px;height:1200px;overflow:hidden;background:var(--paper)}
  body{font-family:"Poppins",Arial,sans-serif;color:var(--ink)}
  .poster{position:relative;width:706px;height:1200px;overflow:hidden}
  .crowd-backdrop{position:absolute;inset:0;
    background:radial-gradient(ellipse at 85% 45%,#d9d4cf 0%,#e9e9eb 45%,#f3f4f6 80%)}
  .shapes{position:absolute;inset:0}
  .brand-row{position:absolute;top:52px;left:462px;display:flex;gap:22px;align-items:center}
  .brand{display:flex;align-items:center;gap:6px;font-weight:700;font-size:19px;color:var(--navy)}
  .brand .dot{width:14px;height:14px;border-radius:50%;background:var(--navy)}
  .brand .square{width:13px;height:13px;background:var(--navy)}
  .title{position:absolute;left:170px;width:370px;top:198px;text-align:center;color:var(--white);line-height:1}
  .title .bold{display:block;font-weight:800;font-size:46px;letter-spacing:-.5px;margin-bottom:12px}
  .title .light{display:block;font-weight:400;font-size:47px;letter-spacing:.5px}
  .tagline{position:absolute;top:408px;left:145px;width:410px;height:30px;text-align:center;
    color:var(--white);font-size:17px;line-height:30px;font-weight:400}
  .date{position:absolute;left:253px;width:200px;text-align:center;top:484px;line-height:1}
  .date .days{display:block;font-weight:800;font-size:36px}
  .date .month{display:block;font-weight:800;font-size:37px;margin-top:6px}
  .date .year{display:block;font-weight:400;font-size:15px;margin-top:6px}
  .pin{position:absolute;left:342px;top:627px}
  .venue{position:absolute;left:100px;width:506px;top:670px;text-align:center;font-weight:800;font-size:33px;line-height:30px;letter-spacing:-.3px}
  .worship{position:absolute;left:484px;top:505px;font-weight:800;font-size:23px;line-height:1.3}
  .worship .hashtag{display:block;margin-top:14px}
  .speakers{position:absolute;top:797px;left:86px;display:flex;gap:57px}
  .speaker{width:142px;text-align:center}
  .speaker .portrait{width:142px;height:176px;border-radius:16px}
  .speaker:nth-child(1) .portrait{background:linear-gradient(160deg,#8fb3c9,#5d9bb8 55%,#3d5f78)}
  .speaker:nth-child(2) .portrait{background:linear-gradient(160deg,#efe9e3,#c8a27c 55%,#f2eee9)}
  .speaker:nth-child(3) .portrait{background:linear-gradient(160deg,#5a4a3f,#2b3040 60%,#1c2230)}
  .speaker .name{margin-top:12px;font-size:14px;font-weight:400}
  .footer-info{position:absolute;left:62px;top:1076px;color:var(--white);font-size:13.5px;line-height:17px}
  .contact{position:absolute;left:468px;top:1100px;color:var(--white);font-size:14px;line-height:21px}
  .contact li{list-style:none;display:flex;align-items:center;gap:24px}
</style>
</head>
<body>
<main class="poster">
  <div class="crowd-backdrop" role="img" aria-label="Soft faded photo of smiling teens gathered together"></div>

  <svg class="shapes" viewBox="0 0 706 1200" width="706" height="1200" aria-hidden="true">
    <polygon points="0,0 271,0 0,531" fill="var(--sky)"/>
    <polygon points="271,0 449,0 200,420 60,420" fill="var(--indigo)"/>
    <polygon points="293,0 449,0 379,144" fill="var(--navy)"/>
    <polygon points="0,531 215,464 153,588 173,635 0,950" fill="var(--indigo)" opacity=".92"/>
    <polygon points="0,531 60,464 37,464 0,600" fill="var(--royal)"/>
    <polygon points="153,588 173,635 0,950 0,1042 370,1042" fill="#e4e6ee" opacity=".55"/>
    <path d="M223,153 H564 Q594,153 594,183 V434 Q594,464 564,464 H37 Z" fill="var(--navy)"/>
    <polygon points="145,408 554,408 546,438 153,438" fill="var(--royal)"/>
    <polygon points="153,438 160,428 161,438" fill="var(--sky)"/>
    <polygon points="546,438 554,426 552,438" fill="var(--sky)"/>
    <polygon points="0,1042 370,1042 379,1051 0,1051" fill="var(--royal)"/>
    <polygon points="0,1051 379,1051 446,1200 0,1200" fill="var(--navy)"/>
    <polygon points="386,1073 706,1073 706,1200 446,1200" fill="var(--royal)"/>
  </svg>

  <div class="brand-row">
    <span class="brand"><span class="dot"></span>Lumenward</span>
    <span class="brand"><span class="square"></span>QRV</span>
  </div>

  <h1 class="title">
    <span class="bold">Harbor Crest<br>Youth</span>
    <span class="light">Conference</span>
  </h1>
  <p class="tagline">Discover new business opportunities</p>

  <p class="date"><span class="days">1-3</span><span class="month">November</span><span class="year">2024</span></p>

  <svg class="pin" width="22" height="30" viewBox="0 0 22 30" aria-hidden="true">
    <path d="M11 0C5 0 0 4.8 0 10.6 0 18 11 30 11 30s11-12 11-19.4C22 4.8 17 0 11 0z" fill="var(--pin)"/>
    <circle cx="11" cy="10.5" r="4.2" fill="var(--white)"/>
  </svg>

  <p class="venue">Tellwood Exhibit Hall<br>Sioux Falls, SD</p>

  <p class="worship">Worship:<br>KW Collective<span class="hashtag">#742GR</span></p>

  <section class="speakers">
    <figure class="speaker">
      <div class="portrait" role="img" aria-label="Portrait of speaker Marcus Linden in a light blue shirt holding a microphone"></div>
      <figcaption class="name">Marcus Linden</figcaption>
    </figure>
    <figure class="speaker">
      <div class="portrait" role="img" aria-label="Portrait of speaker Tessa Vandermeer in a white sweater"></div>
      <figcaption class="name">Tessa Vandermeer</figcaption>
    </figure>
    <figure class="speaker">
      <div class="portrait" role="img" aria-label="Portrait of speaker Colin Hardy in a dark sweater"></div>
      <figcaption class="name">Colin Hardy</figcaption>
    </figure>
  </section>

  <p class="footer-info">For more information or<br>registration please visit<br>HarborCrestGather.com</p>

  <ul class="contact">
    <li>
      <svg width="13" height="13" viewBox="0 0 24 24" aria-hidden="true"><path d="M6.6 10.8a15 15 0 0 0 6.6 6.6l2.2-2.2c.3-.3.7-.4 1-.2 1.1.4 2.3.6 3.6.6.6 0 1 .4 1 1V20c0 .6-.4 1-1 1A17 17 0 0 1 3 4c0-.6.4-1 1-1h3.5c.6 0 1 .4 1 1 0 1.3.2 2.5.6 3.6.1.3 0 .7-.2 1z" fill="var(--white)"/></svg>
      <span>+555-014-2290</span>
    </li>
    <li>
      <svg width="13" height="11" viewBox="0 0 24 18" aria-hidden="true"><path d="M0 0h24v18H0z" fill="var(--white)"/><path d="M0 0l12 9 12-9" stroke="var(--royal)" stroke-width="2" fill="none"/></svg>
      <span>hello@lumenward.org</span>
    </li>
  </ul>
</main>
</body>
</html>
```